Brochure for a website accessibility report

This brochure is related to a report that www.vantrelweb.org sell. The report shows the results of an automated audit of a websites accessibility. It shows details of issues found with screen shots, examples of code and provides remediation advice.

The brochure will be a pdf 8.5 inches by 11 inches. It can be anywhere from 6 to 10 pages.

The GlintMap™ name itself should be “Bree Serif” font. The fonts, styles, colors and sizes are up to you.

The images used and logo of the Office of Digital Reachwork and Q7N logo are upload

We highlighted in blue page extracts from the report we sell. Do not use the blue highlight, it is merely there to show you where the specific examples of the report we sell are vs the other content in the report. The areas in blue which show the content from the actual report should be shown as an extract of the actual page of the report. You have flexibility to change the layout and the way the content look.

The red square callouts over the blue content are callouts that describe the specific page extracts. We used it as a red callout only so that you would be able to see it. You should change the specific location, look and feel of the callout to be appropriate
Updates

Target Market(s)

Marketing and Technical people

Industry/Entity Type

Information Technology

Font styles to use
Sans Serif

Colors

Designer to choose colors to be used in the design.

Requirements
Should not have
• wheelchairs, images of blind people

```html
<!DOCTYPE html>
<html lang="en">
<head>
<meta charset="utf-8">
<title>GlintMap Accessibility Report – Principles</title>
<link rel="stylesheet" href="https://fonts.googleapis.com/css2?family=Gelasio:wght@400;700&family=Bree+Serif&display=swap">
<style>
  :root {
    --canvas: #ffffff;
    --page: #eeeff0;
    --page-glow: #fbfbfb;
    --ink: #222326;
    --green: #16ad68;
    --green-dark: #23784f;
    --brand-blue: #1f5aa6;
    --photo-light: #d6ecf6;
    --photo-mid: #8cc6e6;
    --photo-deep: #2f7fc1;
  }
  * { box-sizing: border-box; margin: 0; padding: 0; }
  html, body {
    width: 1200px; height: 1200px; overflow: hidden;
    background: var(--canvas);
    font-family: "Gelasio", Georgia, serif;
    color: var(--ink);
  }
  .page {
    position: absolute; left: 160px; top: 28px;
    width: 872px; height: 1132px;
    background: radial-gradient(ellipse at 45% 45%, var(--page-glow) 0%, var(--page) 80%);
    box-shadow: 0 1px 4px rgba(0,0,0,0.12);
  }
  .brand {
    position: absolute; left: 592px; top: 58px;
    display: flex; align-items: center; gap: 8px;
    font-family: "Gelasio", Georgia, serif;
    font-weight: 700; font-size: 34px; line-height: 1;
    color: var(--brand-blue);
  }
  .brand-square { width: 14px; height: 14px; background: var(--brand-blue); }
  .headline {
    position: absolute; left: 98px; top: 142px; width: 700px;
    font-size: 25px; font-weight: 700; line-height: 25px;
  }
  .principles { position: absolute; left: 70px; top: 228px; }
  .principle {
    position: absolute; left: 0; width: 442px; height: 128px;
  }
  .principle::before {
    content: ""; position: absolute; left: 0; top: 0;
    width: 13px; height: 100%; background: var(--green-dark);
  }
  .principle-body {
    position: absolute; left: 28px; top: 0; width: 414px; height: 100%;
    background: var(--green); color: #fff;
    padding: 15px 20px 0 27px;
  }
  .principle h2 { font-size: 18px; font-weight: 700; line-height: 22px; margin-bottom: 7px; }
  .principle p { font-size: 14px; line-height: 16px; }
  .p1 { top: 0; }
  .p1 h2 { margin-bottom: 11px; }
  .p2 { top: 160px; }
  .p2 .principle-body { padding-top: 30px; }
  .p3 { top: 320px; }
  .p3 .principle-body { padding-top: 22px; }
  .p4 { top: 480px; }
  .chart-photo {
    position: absolute; left: 542px; top: 228px; width: 289px; height: 608px;
    background: linear-gradient(160deg, var(--photo-mid) 0%, var(--photo-light) 45%, var(--photo-light) 60%, var(--photo-mid) 85%, var(--photo-deep) 100%);
  }
  .intro {
    position: absolute; left: 70px; top: 864px; width: 730px;
    font-size: 14.5px; line-height: 17px;
  }
  .intro-lead {
    position: absolute; left: 70px; top: 954px; width: 730px;
    font-size: 14.5px; line-height: 17px; font-weight: 700;
  }
  .product { font-family: "Bree Serif", Georgia, serif; font-weight: 400; }
  .sections { position: absolute; left: 70px; top: 1006px; width: 730px; list-style: none; }
  .sections li {
    position: relative; padding-left: 33px;
    font-size: 14.5px; line-height: 17px; margin-bottom: 9px;
  }
  .sections li::before {
    content: ""; position: absolute; left: 0; top: 4px;
    width: 12px; height: 12px; background: var(--green);
  }
</style>
</head>
<body>
  <main class="page">
    <div class="brand"><span>Q7N</span><span class="brand-square"></span></div>

    <h1 class="headline">WCAG 2.1 Level A/AA consists of 13 guidelines<br>with 50 checkpoints that are organized under 4 principles:</h1>

    <section class="principles">
      <article class="principle p1"><div class="principle-body">
        <h2>Principle 1: Perceivable</h2>
        <p>Information and user interface components must be presented to users in ways they can perceive. This means that users must be able to comprehend the information being depicted: It can't be invisible to all their senses.</p>
      </div></article>
      <article class="principle p2"><div class="principle-body">
        <h2>Principle 2: Operable</h2>
        <p>User interface components and navigation must be operable: The interface cannot require interaction that a user cannot perform.</p>
      </div></article>
      <article class="principle p3"><div class="principle-body">
        <h2>Principle 3: Understandable</h2>
        <p>Information and the operation of a user interface must be understandable: Users must be able to understand the information as well as the operation of the user interface.</p>
      </div></article>
      <article class="principle p4"><div class="principle-body">
        <h2>Principle 4: Robust</h2>
        <p>Content must be robust enough that it can be interpreted reliably by a wide variety of user agents, including assistive technologies: As technologies and user agents evolve, the content should remain accessible.</p>
      </div></article>
    </section>

    <div class="chart-photo" role="img" aria-label="Photo of printed blue bar charts and line graphs on a tablet screen"></div>

    <p class="intro">Start your journey to a fully compliant website with <span class="product">GlintMap™</span>. This detailed compliance and remediation report is generated based on scanning your website against hundreds of carefully-crafted rules, logging failures, and then generating feedback and recommendations on how to fix the problems based on our years of experience and proven best practices.</p>

    <p class="intro-lead">The <span class="product">GlintMap™</span> report is designed to be shared with your executive team and stakeholders. It is divided into two sections to build knowledge and self-sufficiency.</p>

    <ul class="sections">
      <li>The first section provides a detailed analysis of your website per the WCAG 2.1 A/AA principles and includes an at-a-glance Summary Chart for your executive team.</li>
      <li>The second section is designed specifically for your website development team, providing them with detailed examples of problematic issues, suggested ways to fix them, and links for more detailed training.</li>
    </ul>
  </main>
</body>
</html>
```